NZ First of it's kind solutions directory and marketplace for busy Mums needs a business card design

We need a business card design for our new nationwide business in NZ (long term plans to go global). We provide solutions to the everyday challenges that busy Mums face by connecting them with quality communities and suppliers of carefully selected, relevant products and services. We sell direct via our online marketplace. The final design should communicate our values of inclusivity, quality and smart solutions. Colours should incorporate our logo colour palette of #477077 and #6ba8b2. Our website is at https://www.brightnestly.com

Target Market(s)

busy Mums, Age 28 – 50, female, income over $100K, location main centres NZ primarily but NZ wide. Is likely juggling work or career with a young family. Probably had hobbies which have fallen by the wayside.
-Wants to succeed in her chosen career without compromising on family life
-to successfully juggle her career without feeling like she is compromising her children
- Is time poor, something always has to give and it’s generally her health (she’ll stay up late, get stressed)
- probably ex corporate or professional career. Has discretional income

Industry/Entity Type

Business

Contact Information for Business Card

Jodie Farnsworth, Founder, BrightNestly.com (Strapline Browse; Pick; Sorted), 48 Kowhai Terrace, Hillsborough, Auckland 1058, New Zealand. Mob: 021 437 518 Ph: +64 (0)9 584 7163

Font styles to use
Other font styles liked:
• Raleway, and/or Architects Daughter

Colors
00a990
33b8a4
86cfc6
cfeae6

Requirements
Must have
• the above details, streamline. the logo and colours associated with those logos
Should not have
• foil or metallic colours

```html
<!DOCTYPE html>
<html lang="en">
<head>
<meta charset="utf-8">
<title>BrightNestly — Business Card</title>
<link href="https://fonts.googleapis.com/css2?family=Roboto:wght@400;500&family=Roboto+Condensed:wght@700&display=swap" rel="stylesheet">
<style>
  :root{
    --backdrop:#e9e6e1;
    --card-white:#fbfbfb;
    --teal-deep:#477077;
    --teal-light:#6ba8b2;
    --ink:#4a4d50;
    --rule:#9a9a9a;
  }
  *{margin:0;padding:0;box-sizing:border-box}
  html,body{width:1200px;height:886px;overflow:hidden}
  body{
    background:var(--backdrop);
    font-family:"Roboto",Arial,sans-serif;
    display:flex;align-items:center;justify-content:center;gap:60px;
  }
  .card{
    width:520px;height:300px;border-radius:22px;position:relative;
    box-shadow:0 8px 24px rgba(0,0,0,.18);
    overflow:hidden;
  }
  .card--front{background:var(--card-white)}
  .card--back{
    background:var(--teal-deep);
    display:flex;align-items:center;justify-content:center;
  }
  .identity{position:absolute;left:40px;top:44px;width:250px}
  .identity__name{
    font-family:"Roboto Condensed",Arial,sans-serif;font-weight:700;
    font-size:25px;letter-spacing:-.3px;color:var(--teal-deep);
    text-transform:uppercase;line-height:1;
  }
  .identity__role{
    font-size:15px;color:var(--teal-light);text-transform:uppercase;
    margin-top:4px;letter-spacing:.3px;
  }
  .divider{border:0;border-top:1.5px dotted var(--rule);margin:14px 0 12px;width:230px}
  .address{font-size:14px;color:var(--ink);line-height:1.45}
  .contacts{list-style:none;font-size:14px;color:var(--ink);line-height:1.45}
  .contacts li{display:flex;align-items:center;gap:8px}
  .contacts svg{width:11px;height:11px;flex:none}
  .front-mark{
    position:absolute;right:36px;top:50px;width:170px;height:120px;
    display:flex;align-items:center;justify-content:center;
  }
  .front-mark span,.back-mark{
    font-family:"Roboto",Arial,sans-serif;font-weight:500;
    letter-spacing:-.5px;
  }
  .front-mark span{font-size:30px;color:var(--teal-deep)}
  .back-mark{font-size:52px;color:#ffffff}
</style>
</head>
<body>
  <article class="card card--front">
    <div class="front-mark"><span>BrightNestly</span></div>
    <div class="identity">
      <h1 class="identity__name">Jodie Farnsworth</h1>
      <p class="identity__role">Founder</p>
      <hr class="divider">
      <p class="address">48 Kowhai Terrace, Hillsborough<br>Auckland 1058, New Zealand.</p>
      <hr class="divider">
      <ul class="contacts">
        <li><svg viewBox="0 0 12 12" aria-hidden="true"><path d="M2.5 1 L4.5 1 L5 3.5 L3.8 4.5 Q5 7 7.5 8.2 L8.5 7 L11 7.5 L11 9.5 Q10.5 11 9 11 Q1 10 1 2.5 Q1 1 2.5 1Z" fill="var(--teal-deep)"/></svg>+64 (0)9 584 7163</li>
        <li><svg viewBox="0 0 12 12" aria-hidden="true"><rect x="3" y="1" width="6" height="10" rx="1" fill="none" stroke="var(--teal-deep)" stroke-width="1.4"/></svg>021 437 518</li>
        <li><svg viewBox="0 0 12 12" aria-hidden="true"><circle cx="6" cy="6" r="5" fill="var(--teal-deep)"/><path d="M1 6 H11 M6 1 Q3 6 6 11 Q9 6 6 1" fill="none" stroke="#fff" stroke-width=".8"/></svg>BrightNestly.com</li>
      </ul>
    </div>
  </article>

  <article class="card card--back">
    <span class="back-mark">BrightNestly</span>
  </article>
</body>
</html>
```